依頼詳細
【 デザインイメージ 】
・主に男性向けで、高級感がある、尿酸サプリにしたいです。
・ターゲット層:50~60代の男性
・色のイメージ 黄色か・金色 + α
・商品画像をパッと見て 「高級感」「イメージしやすさ」「しっかり入っていそう」とわかりやすいもの

※本品は「機能性表示食品」です そのため恐れ入りますが、暮らし安全局からの差し戻しにより、
軽微なテキスト修正などが、半年間ほどの間に2回ほど発生する可能性があります

・詳細は添付ファイルをご参考ください。
【 依頼内容 】
・ラベル ラベルサイズ 縦110 * 横80 (白いアルミチャック袋にラベルを貼ります)

・詳細は添付ファイルをご参考ください。

▼重要視する点・経験
・サプリメント、化粧品等のパッケージデザインをした経験

▼注意点・禁止事項
※他で登録されているデザインや商標の転用など、他社の知的財産権、著作権を侵すこと
※他のクライアントへ既に提案した内容の転用など

作成して頂くパッケージのデザインについてご質問等ありましたら、お気軽にご連絡下さい。
たくさんのデザイナー・クリエイターの方々からの応募をお待ちしております!
希望イメージ
シンプル 複雑
単色 カラフル
暗い 明るい
日常 高級
遊び心 厳粛
未来的 伝統的
女性的 男性的
希望する色
青系、黄・オレンジ系、尿酸なので、黄色がイメージしやすいと思っています… 詳細は添付資料をご覧ください
納品ファイル
• 高解像度JPG (.jpg)
• イラストレーター形式 (.ai)
補足説明
■ 選んだ理由

どのご提案も弊社の希望を盛り込んで頂いておりましたが、こちらのデザイン案は、
社内で「男性票」が一番多く入り、希望したテイストに仕上がっていた点が採用の決め手になりました。

■ 提案者全員のお礼・コメント

この度は多数のご提案ありがとうございました!
機能性表示食品の「規定」もある程度ふまえて選択させていただきましたが
どのデザイン案も素敵なものばかりでした。
また機会がございましたらよろしくお願い申し上げます。

```html
<!DOCTYPE html>
<html lang="ja">
<head>
<meta charset="utf-8">
<title>尿酸スマートケア ラベル</title>
<link rel="stylesheet" href="https://fonts.googleapis.com/css2?family=Noto+Sans+JP:wght@400;500;700;900&display=swap">
<style>
  :root {
    --ink: #111111;
    --band-dark: #0d0d0d;
    --band-mid: #2a2a2a;
    --gold: #f2c21a;
    --gold-deep: #c99a0c;
    --gold-light: #ffe58a;
    --paper: #ffffff;
    --paper-shade: #eeeeee;
    --body-text: #333333;
    --flower-main: #f6cf2a;
    --flower-soft: #fff3b8;
  }
  * { margin: 0; padding: 0; box-sizing: border-box; }
  html, body { width: 874px; height: 1200px; overflow: hidden; }
  body { font-family: "Noto Sans JP", sans-serif; background: var(--paper); }

  .label {
    position: relative;
    width: 874px; height: 1200px;
    background: linear-gradient(180deg, var(--paper) 0%, var(--paper-shade) 45%, var(--paper) 70%);
    overflow: hidden;
  }

  .top-band {
    position: absolute; left: 0; top: 0; width: 874px; height: 96px;
    background: linear-gradient(180deg, var(--band-mid), var(--band-dark));
    display: flex; align-items: center; justify-content: center;
  }
  .top-band__text {
    color: var(--gold); font-weight: 900; font-size: 58px; letter-spacing: 2px; line-height: 1;
  }

  .headline {
    position: absolute; left: 28px; top: 100px;
    font-weight: 900; color: var(--ink); line-height: 1;
    white-space: nowrap;
  }
  .headline__main { font-size: 196px; letter-spacing: -4px; }
  .headline__particle { font-size: 150px; }

  .product-name {
    position: absolute; left: 80px; top: 300px; width: 310px; height: 56px;
    background: var(--ink); color: var(--paper);
    font-weight: 700; font-size: 34px; line-height: 1;
    white-space: nowrap;
    display: flex; align-items: center; justify-content: center;
  }
  .headline-tail {
    position: absolute; left: 420px; top: 284px;
    font-weight: 900; font-size: 116px; color: var(--ink); line-height: 1;
    white-space: nowrap;
  }

  .flower-visual {
    position: absolute; left: 0; top: 410px; width: 690px; height: 270px;
    background: radial-gradient(ellipse at 45% 50%, var(--flower-main) 0%, var(--gold) 40%, var(--flower-soft) 75%, rgba(255,255,255,0) 100%);
  }

  .serving-badge {
    position: absolute; left: 686px; top: 466px; width: 166px; height: 166px;
    border-radius: 50%;
    background: radial-gradient(circle at 35% 30%, var(--gold-light), var(--gold) 55%, var(--gold-deep));
    border: 3px solid #fff;
    display: flex; flex-direction: column; align-items: center; justify-content: center;
    color: var(--ink); text-align: center; line-height: 1.05;
  }
  .serving-badge__period { font-size: 20px; font-weight: 700; }
  .serving-badge__count { font-size: 56px; font-weight: 900; }
  .serving-badge__count small { font-size: 28px; }
  .serving-badge__dose { font-size: 14px; font-weight: 500; margin-top: 2px; }

  .ingredient-bar {
    position: absolute; left: 44px; top: 690px; width: 830px; height: 48px;
    background: linear-gradient(90deg, var(--gold-deep), var(--gold) 35%, var(--gold-light) 70%, rgba(255,229,138,0));
    display: flex; align-items: center; padding-left: 22px;
    font-weight: 900; font-size: 30px; color: var(--ink); white-space: nowrap;
  }

  .claim {
    position: absolute; left: 0; top: 752px; width: 874px;
    text-align: center; font-size: 26px; font-weight: 500; line-height: 1.5;
    color: var(--body-text);
  }

  .notice {
    position: absolute; left: 0; top: 890px; width: 874px; height: 310px;
    background: linear-gradient(180deg, var(--band-mid), var(--band-dark));
    padding: 22px 30px 0;
    color: var(--paper);
  }
  .notice__title { font-size: 29px; font-weight: 700; color: var(--gold); white-space: nowrap; }
  .notice__title span { color: var(--paper); margin-left: 14px; }
  .notice__body { margin-top: 10px; font-size: 27px; line-height: 1.6; }
</style>
</head>
<body>
<main class="label">
  <header class="top-band"><p class="top-band__text">尿酸値が高めな方の</p></header>

  <h1 class="headline"><span class="headline__main">尿酸値</span><span class="headline__particle">を</span></h1>
  <p class="product-name">尿酸スマートケア</p>
  <p class="headline-tail">下げる</p>

  <div class="flower-visual" role="img" aria-label="ざるに盛られた黄色い菊の花"></div>

  <div class="serving-badge">
    <span class="serving-badge__period">約1ヶ月分</span>
    <span class="serving-badge__count">90<small>粒</small></span>
    <span class="serving-badge__dose">1日摂取<br>目安量：3粒</span>
  </div>

  <p class="ingredient-bar">菊の花由来「ルテオリン」</p>

  <p class="claim">本品には、(菊の花由来）ルテオリンが含まれます。<br>(菊の花由来)ルテオリンには尿酸値が高めな方の<br>尿酸値を下げる機能が報告されています。</p>

  <section class="notice">
    <p class="notice__title">機能性表示食品<span>届出番号●●●●</span></p>
    <p class="notice__body">本品は、事業者の責任において特定の保健の目的が期待できる旨を表示するものとして、暮らし安全局長官に届出されたものです。ただし、特定保健用食品と異なり、暮らし安全局長官による個別審査を受けたものではありません。</p>
  </section>
</main>
</body>
</html>
```